Business Card Design - cloud video monitoring

For the trade show in Las Vegas our company needs business cards with new brand - Vantrolux

The logo of the new brand is attached, the sample card with the founder's contact details is attached (just change the website to www.vantrolux.me) and email to info@vantrolux.me
Updates

                                        Forgot to say: the tagline for the brand is "the new normal cloud video management"

Industry/Entity Type

Business

```html
<!DOCTYPE html>
<html lang="en">
<head>
<meta charset="utf-8">
<title>Vantrolux Business Card</title>
<link rel="stylesheet" href="https://fonts.googleapis.com/css2?family=PT+Serif:wght@400;700&display=swap">
<style>
  :root {
    --page-bg: #e9e7e3;
    --charcoal: #3c3c3e;
    --teal: #36bda3;
    --paper: #ffffff;
    --ink: #2b2b2b;
    --muted: #8a8a8a;
    --hairline: rgba(255,255,255,0.12);
  }
  html, body {
    margin: 0;
    width: 1200px;
    height: 900px;
    overflow: hidden;
    background: var(--page-bg);
    font-family: "PT Serif", Georgia, serif;
  }
  .card {
    position: absolute;
    left: 180px;
    top: 210px;
    width: 840px;
    height: 480px;
    background: var(--charcoal);
    overflow: hidden;
    box-shadow: 0 10px 30px rgba(0,0,0,0.18);
  }
  .card__rule {
    position: absolute;
    left: 0;
    width: 360px;
    height: 1px;
    background: var(--hairline);
  }
  .card__rule--top { top: 70px; }
  .card__rule--bottom { top: 410px; }
  .brand {
    position: absolute;
    left: 60px;
    top: 200px;
    display: flex;
    align-items: center;
    gap: 20px;
  }
  .brand__dot {
    width: 72px;
    height: 72px;
    border-radius: 50%;
    background: var(--teal);
  }
  .brand__name {
    font-size: 44px;
    font-weight: 400;
    color: var(--teal);
    letter-spacing: 1px;
  }
  .card__accent {
    position: absolute;
    left: 372px;
    top: 0;
    right: 0;
    bottom: 0;
    background: var(--teal);
    border-radius: 40px 0 0 40px;
  }
  .card__panel {
    position: absolute;
    left: 394px;
    top: 0;
    right: 0;
    bottom: 0;
    background: var(--paper);
    border-radius: 40px 0 0 40px;
  }
  .person {
    position: absolute;
    left: 64px;
    top: 90px;
  }
  .person__name {
    margin: 0;
    font-size: 32px;
    font-weight: 400;
    color: var(--ink);
  }
  .person__role {
    margin: 6px 0 0;
    font-size: 20px;
    color: var(--muted);
  }
  .contact {
    position: absolute;
    left: 64px;
    top: 248px;
    margin: 0;
    display: grid;
    grid-template-columns: 80px auto;
    row-gap: 10px;
    font-size: 19px;
  }
  .contact dt {
    font-weight: 700;
    color: var(--ink);
  }
  .contact dd {
    margin: 0;
    color: var(--muted);
  }
  .contact__extra {
    grid-column: 1 / 3;
    font-weight: 700;
    color: var(--ink);
  }
</style>
</head>
<body>
  <div class="card">
    <span class="card__rule card__rule--top"></span>
    <span class="card__rule card__rule--bottom"></span>
    <div class="brand">
      <span class="brand__dot"></span>
      <span class="brand__name">Vantrolux</span>
    </div>
    <div class="card__accent"></div>
    <div class="card__panel">
      <div class="person">
        <h1 class="person__name">Marek Dolansky</h1>
        <p class="person__role">Founder</p>
      </div>
      <dl class="contact">
        <dt>Tel:</dt><dd>+1 647 555 0142</dd>
        <dt>Fax:</dt><dd>+1 416 555 0187</dd>
        <dt>Email:</dt><dd>www.vantrolux.me</dd>
        <dd class="contact__extra">info@vantrolux.me</dd>
      </dl>
    </div>
  </div>
</body>
</html>
```